Real Estate Renovation and Rental:Business Card/Logo Design Project

Corliss Grove LLC is a small partnership that buys homes to renovate, then provide as rentals to people who may not currently be able to purchase a home - but we also coach them on how to improve their credit so that, in 2-5 years, they may be able to buy a home. Maybe even the one they're living in.

We are based in Sonoma County of Northern California, operating in communities including Healdsburg, Windsor, Santa Rosa, and Cloverdale.

Please design a business card, but the same logo should work for signs that we will post on the homes as they are being renovated.

The design should be clean, contemporary, professional but warm. I'd love to see a rooftop feature, or some other element of a house. Again, not too much detail, clean and welcoming. The design must include "Corliss Grove LLC" - but "CGLLC" could also be used as a primary name, with "Corliss Grove LLC" in smaller print somewhere. If using "CGLLC", the CG could be visually distinct (larger, different color, font) than the LLC part of the name but they must be together.
Updates

just conferring with partner to choose a final design ... should be ready to choose soon and will post

Industry/Entity Type

Business

Requirements
Must have
• the name "Corliss Grove LLC"
for business card design, and leave room for us to customize with partner names, address, telephone numbers, email addresses
Nice to have
• some element of a house included

```html
<!DOCTYPE html>
<html lang="en">
<head>
<meta charset="utf-8">
<title>Corliss Grove LLC – Business Card</title>
<link rel="stylesheet" href="https://fonts.googleapis.com/css2?family=Playfair+Display:wght@900&family=Rokkitt:wght@400&family=Tinos&display=swap">
<style>
  :root {
    --card-teal: #358b7f;
    --ink: #111111;
    --white: #ffffff;
    --brand-red: #ff1a00;
    --strip-light: #cfcfcf;
    --strip-mid: #a6a6a6;
    --strip-dark: #7a7a7a;
    --strip-deep: #4b4b4b;
  }
  html, body {
    margin: 0;
    padding: 0;
    width: 1200px;
    height: 686px;
    overflow: hidden;
    background: var(--card-teal);
  }
  .card {
    position: relative;
    width: 1200px;
    height: 686px;
    background: var(--card-teal);
    overflow: hidden;
  }
  .company-name {
    position: absolute;
    left: 86px;
    top: 80px;
    margin: 0;
    font-family: "Playfair Display", "Times New Roman", serif;
    font-weight: 900;
    font-size: 70px;
    line-height: 1;
    letter-spacing: 8px;
    color: var(--ink);
    text-shadow: 4px 4px 6px rgba(0, 0, 0, 0.45);
    white-space: nowrap;
  }
  .tagline {
    position: absolute;
    width: 300px;
    margin: 0;
    text-align: center;
    font-family: "Tinos", "Times New Roman", serif;
    font-size: 31px;
    line-height: 1;
    color: var(--ink);
    white-space: nowrap;
  }
  .tagline--top { left: 120px; top: 220px; }
  .tagline--bottom { left: 110px; top: 488px; }
  .brand-mark {
    position: absolute;
    left: 131px;
    top: 340px;
    width: 260px;
    display: flex;
    align-items: center;
    gap: 14px;
    font-family: "Rokkitt", Georgia, serif;
    font-size: 62px;
    line-height: 1;
    color: var(--brand-red);
  }
  .brand-mark__square {
    width: 46px;
    height: 46px;
    background: var(--brand-red);
    flex: none;
  }
  .divider {
    position: absolute;
    left: 496px;
    top: 210px;
  }
  .contact {
    position: absolute;
    right: 149px;
    top: 396px;
    text-align: right;
    font-family: "Rokkitt", Georgia, serif;
    font-style: normal;
    color: var(--ink);
  }
  .contact__name {
    margin: 0 0 4px;
    font-size: 52px;
    font-weight: 400;
    line-height: 62px;
    color: var(--white);
  }
  .contact__line {
    margin: 0;
    font-size: 39px;
    line-height: 50px;
  }
  .edge-strip {
    position: absolute;
    top: 0;
    right: 0;
    height: 686px;
    display: flex;
  }
  .edge-strip span { display: block; height: 100%; }
  .edge-strip__light { width: 17px; background: var(--strip-light); }
  .edge-strip__mid { width: 17px; background: var(--strip-mid); }
  .edge-strip__dark { width: 17px; background: var(--strip-dark); }
  .edge-strip__deep { width: 80px; background: var(--strip-deep); }
</style>
</head>
<body>
<main class="card">
  <h1 class="company-name">CORLISS GROVE LLC</h1>

  <p class="tagline tagline--top">Restoring Houses</p>
  <div class="brand-mark">
    <span class="brand-mark__square"></span>
    <span class="brand-mark__name">CGLLC</span>
  </div>
  <p class="tagline tagline--bottom">Renewing Futures…</p>

  <svg class="divider" width="14" height="356" viewBox="0 0 14 356" aria-hidden="true">
    <line x1="7" y1="6" x2="7" y2="350" stroke="#111" stroke-width="2"/>
    <path d="M7 1 L11 6 L7 11 L3 6 Z" fill="none" stroke="#111" stroke-width="1.5"/>
    <path d="M7 345 L11 350 L7 355 L3 350 Z" fill="none" stroke="#111" stroke-width="1.5"/>
  </svg>

  <address class="contact">
    <p class="contact__name">Alex R. Moreno, Owner</p>
    <p class="contact__line">(707) 555-0148</p>
    <p class="contact__line">412 Vine Street</p>
    <p class="contact__line">Santa Rosa, CA&nbsp;&nbsp;95401</p>
    <p class="contact__line">alex@corlissgrove.com</p>
  </address>

  <div class="edge-strip" aria-hidden="true">
    <span class="edge-strip__light"></span>
    <span class="edge-strip__mid"></span>
    <span class="edge-strip__dark"></span>
    <span class="edge-strip__deep"></span>
  </div>
</main>
</body>
</html>
```